Financial Service Company Need Business Card Design

This is a new startup company, first of its kind to offer this service. We facilitate the movement of deposit funds electronically between home buyers and real estate brokerages.Our customers are DOMIVANS®, real estate brokerages, and home buyers, we identify ourselves as a financial/technology company.
Not looking for anything too flashy. Just a clean design that shows the logo, contact info, etc. Company colors can be seen on attached logo, and 'coming soon page'
www.quorvanta.ca

```html
<!DOCTYPE html>
<html lang="en">
<head>
<meta charset="utf-8">
<title>Quorvanta Business Card</title>
<link href="https://fonts.googleapis.com/css2?family=Mulish:wght@400;600;700&display=swap" rel="stylesheet">
<style>
  :root {
    --backdrop: #4b4b4d;
    --card-light: #f7f7f5;
    --card-dark-top: #55555a;
    --card-dark-bottom: #404044;
    --brand-red: #d9432a;
    --ink-grey: #59595b;
    --rule-grey: #8a8a8a;
    --on-dark: #f2f2f2;
    --on-dark-soft: #c9c9cc;
  }
  * { margin: 0; padding: 0; box-sizing: border-box; }
  html, body {
    width: 1200px; height: 1000px; overflow: hidden;
    background: var(--backdrop);
    font-family: "Mulish", "Century Gothic", sans-serif;
  }
  .canvas { position: relative; width: 1200px; height: 1000px; }

  .card {
    position: absolute;
    width: 528px; height: 300px;
    border-radius: 14px;
  }
  .card--front { left: 207px; top: 165px; background: var(--card-light); }
  .card--back {
    left: 473px; top: 551px;
    background: linear-gradient(160deg, var(--card-dark-top), var(--card-dark-bottom));
  }

  .wordmark {
    position: absolute;
    display: flex; align-items: center; gap: 10px;
    font-weight: 600; font-size: 31px; letter-spacing: -0.3px;
    line-height: 1;
  }
  .wordmark__square { width: 30px; height: 30px; background: var(--brand-red); }
  .card--front .wordmark { left: 34px; top: 50px; color: var(--ink-grey); }
  .card--back .wordmark { right: 48px; top: 132px; color: var(--on-dark); }

  .divider {
    position: absolute; left: 34px; top: 105px;
    width: 460px; height: 2px; background: var(--rule-grey);
  }

  .contact {
    position: absolute; left: 34px; top: 220px;
    font-size: 12px; line-height: 15px; color: var(--ink-grey);
  }
  .contact__label { color: var(--brand-red); font-weight: 700; }

  .person {
    position: absolute; right: 34px; top: 218px; text-align: right;
  }
  .person__name {
    font-size: 17.5px; font-weight: 700; color: var(--brand-red);
    letter-spacing: 0.6px; line-height: 22px;
  }
  .person__title { font-size: 14px; color: var(--ink-grey); line-height: 18px; }

  .web {
    position: absolute; right: 48px; top: 186px;
    font-size: 12.5px; color: var(--on-dark-soft); letter-spacing: 0.4px;
  }
</style>
</head>
<body>
<main class="canvas">
  <section class="card card--front">
    <div class="wordmark"><span class="wordmark__square"></span>Quorvanta</div>
    <div class="divider"></div>
    <address class="contact" style="font-style:normal">
      4820 Linden Crest Way, Marlow, FL 33910<br>
      <span class="contact__label">T:</span> (02) 5550-4817 · <span class="contact__label">F:</span> (02) 5550-2263<br>
      <span class="contact__label">E:</span> info@quorvanta.ca.com
    </address>
    <div class="person">
      <div class="person__name">NEIL HARWOOD</div>
      <div class="person__title">General Manager</div>
    </div>
  </section>

  <section class="card card--back">
    <div class="wordmark"><span class="wordmark__square"></span>Quorvanta</div>
    <div class="web">www.quorvanta.ca.com</div>
  </section>
</main>
</body>
</html>
```